Postcard Design

We are an exterior house wash company looking to design postcards to promote our business. we clean all types roofs and all types houses and all types of decks and all types of surfaces with a low pressure soft wash system.we also try to educate customers about the options and offer a maintenance program so their property is never dirty again, we use 100% biodegradable solutions to achieve results! our method outperforms traditional washing methods and remains clean 5 times longer,our method is 100% damage free,never pressure wash again!! our method is recommended by all manufactures,the NO pressure method,this method cleans so good you won't believe your eyes! guaranteed call today 207-555-0148 also want to add residential and commercial work and all hoa's(home owners assoc) also group rates available ,please use house washing logo provided,and roof washing logo,also the name of business is Brightmere exterior house washing thanks

Industry/Entity Type

Biodegradable

Requirements
Must have
• company name (Brightmere exterior house washing),logos provided(house wash,roof wash),also pics provided,thank you

```html
<!DOCTYPE html>
<html lang="en">
<head>
<meta charset="utf-8">
<title>Brightmere Exterior House Washing – Postcard</title>
<link rel="stylesheet" href="https://fonts.googleapis.com/css2?family=Bree+Serif&family=Alegreya+SC:wght@800&family=Open+Sans:wght@600;700&display=swap">
<style>
  :root {
    --navy: #0f4260;
    --ink: #123a5c;
    --sky: #4fb8e8;
    --mist: #dbe4ea;
    --title: #e9f1f6;
    --white: #ffffff;
    --photo-sky: #9fc3d9;
    --photo-house: #8a8f86;
    --photo-lawn: #3f6b2e;
  }
  * { box-sizing: border-box; margin: 0; padding: 0; }
  html, body {
    width: 1200px; height: 1047px; overflow: hidden;
    background: var(--white);
    font-family: "Open Sans", Arial, sans-serif;
  }
  .sheet { position: relative; width: 1200px; height: 1047px; }

  .side-label {
    position: absolute;
    font-family: "Open Sans", Arial, sans-serif;
    font-weight: 700;
    color: var(--navy);
    font-size: 74px;
    line-height: 1;
    letter-spacing: 1px;
  }
  .side-label--front { left: 708px; top: 70px; }
  .side-label--back { left: 159px; top: 626px; }

  .card {
    position: absolute;
    width: 614px; height: 462px;
    background: linear-gradient(to top right, var(--sky) 0%, #8ccbeb 45%, var(--mist) 100%);
    overflow: hidden;
  }
  .card--front { left: 48px; top: 25px; }
  .card--back { left: 547px; top: 555px; }

  .brand-title {
    position: absolute; left: 0; top: 8px; width: 100%;
    text-align: center;
    font-family: "Alegreya SC", Georgia, serif;
    font-weight: 800;
    font-size: 28px;
    color: var(--title);
    letter-spacing: 1px;
    text-shadow: 0 1px 2px rgba(20, 60, 90, 0.35);
  }

  .photo {
    position: absolute; left: 14px; width: 275px; height: 110px;
    background: linear-gradient(to bottom, var(--photo-sky) 0%, var(--photo-sky) 28%, var(--photo-house) 30%, var(--photo-house) 62%, var(--photo-lawn) 66%, #6f9a4f 100%);
  }
  .photo--before { top: 82px; }
  .photo--after { top: 208px; background: linear-gradient(to bottom, #b9d6e8 0%, #b9d6e8 28%, #a9a79c 30%, #b3b1a6 62%, #4f7d34 66%, #79a857 100%); }
  .photo__tag {
    position: absolute; right: 0; bottom: 0;
    background: var(--white);
    color: #222;
    font-size: 8px; font-weight: 600;
    padding: 3px 8px;
  }

  .badge { position: absolute; left: 405px; top: 58px; width: 146px; height: 156px; }
  .badge text { font-family: "Bree Serif", Georgia, serif; fill: var(--ink); font-size: 19px; letter-spacing: 0.5px; }

  .company-name {
    position: absolute; left: 318px; top: 222px; width: 290px;
    text-align: center;
    font-family: "Bree Serif", Georgia, serif;
    font-size: 31px; line-height: 1.08;
    color: var(--ink);
  }

  .call {
    position: absolute;
    display: flex; align-items: center; gap: 8px;
    font-weight: 700; color: var(--navy);
  }
  .call svg { flex: none; }
  .card--front .call { left: 318px; top: 294px; font-size: 19px; }
  .card--back .call { left: 34px; top: 270px; font-size: 19px; }

  .service-row {
    position: absolute; left: 0; width: 100%; height: 116px;
    display: flex; align-items: center;
  }
  .card--front .service-row { top: 335px; }
  .card--back .service-row { top: 343px; }
  .service-mark {
    flex: 1;
    text-align: center;
    font-family: "Open Sans", Arial, sans-serif;
    font-weight: 700;
    font-size: 34px;
    line-height: 1.05;
    color: var(--navy);
    text-transform: uppercase;
  }
  .service-row__divider { width: 7px; height: 100px; background: var(--navy); flex: none; }

  .checklist { position: absolute; left: 34px; top: 62px; width: 560px; list-style: none; }
  .checklist li {
    position: relative;
    padding-left: 30px;
    margin-bottom: 11px;
    font-size: 18px; font-weight: 700; line-height: 1.2;
    color: var(--ink);
  }
  .checklist li svg { position: absolute; left: 0; top: 2px; }
</style>
</head>
<body>
<main class="sheet">

  <section class="card card--front" aria-label="Postcard front">
    <h1 class="brand-title">Brightmere Exterior House Washing</h1>

    <div class="photo photo--before" role="img" aria-label="Photo of a stone ranch house with a stained roof, before cleaning">
      <span class="photo__tag">Before</span>
    </div>
    <div class="photo photo--after" role="img" aria-label="Photo of the same ranch house with a clean roof, after cleaning">
      <span class="photo__tag">After</span>
    </div>

    <svg class="badge" viewBox="0 0 146 156" aria-label="100% damage free">
      <polygon fill="#9ad3ef" stroke="#1b4d70" stroke-width="1.5"
        points="73,2 86,30 112,14 108,45 140,46 116,68 140,92 108,96 114,128 86,113 73,150 60,113 32,128 38,96 6,92 30,68 6,46 38,45 34,14 60,30"/>
      <polygon fill="none" stroke="#ffffff" stroke-width="1"
        points="73,10 84,35 106,22 103,49 131,50 110,68 131,88 103,91 108,119 84,107 73,140 62,107 38,119 43,91 15,88 36,68 15,50 43,49 40,22 62,35"/>
      <text x="73" y="58" text-anchor="middle">100%</text>
      <text x="73" y="79" text-anchor="middle">DAMAGE</text>
      <text x="73" y="100" text-anchor="middle">FREE</text>
    </svg>

    <h2 class="company-name">Exterior House Wash Company</h2>

    <p class="call">
      <svg width="22" height="22" viewBox="0 0 24 24" aria-hidden="true"><circle cx="12" cy="12" r="12" fill="#0b0b0b"/><path fill="#fff" d="M8.2 5.5l2 2.6c.3.4.3.9-.1 1.3l-1 1c.7 1.5 1.9 2.7 3.4 3.4l1-1c.4-.4.9-.4 1.3-.1l2.6 2c.4.3.5.9.1 1.3l-1.2 1.3c-.6.6-1.5.8-2.3.5-3.5-1.3-6.2-4-7.5-7.5-.3-.8-.1-1.7.5-2.3L6.9 5.4c.4-.4 1-.3 1.3.1z"/></svg>
      Call today 207-555-0148
    </p>

    <div class="service-row">
      <p class="service-mark">Roof<br>Cleaning</p>
      <span class="service-row__divider"></span>
      <p class="service-mark">House<br>Washing</p>
    </div>
  </section>

  <span class="side-label side-label--front">FRONT</span>
  <span class="side-label side-label--back">BACK</span>

  <section class="card card--back" aria-label="Postcard back">
    <ul class="checklist">
      <li><svg width="18" height="18" viewBox="0 0 18 18" aria-hidden="true"><rect x="1" y="1" width="16" height="16" rx="2" fill="none" stroke="#123a5c" stroke-width="1.6"/><path d="M4.5 9.2l3 3 6-7" fill="none" stroke="#123a5c" stroke-width="2"/></svg>All types Roofs and all types Houses.</li>
      <li><svg width="18" height="18" viewBox="0 0 18 18" aria-hidden="true"><rect x="1" y="1" width="16" height="16" rx="2" fill="none" stroke="#123a5c" stroke-width="1.6"/><path d="M4.5 9.2l3 3 6-7" fill="none" stroke="#123a5c" stroke-width="2"/></svg>Decks and all types of Surfaces.</li>
      <li><svg width="18" height="18" viewBox="0 0 18 18" aria-hidden="true"><rect x="1" y="1" width="16" height="16" rx="2" fill="none" stroke="#123a5c" stroke-width="1.6"/><path d="M4.5 9.2l3 3 6-7" fill="none" stroke="#123a5c" stroke-width="2"/></svg>Low Pressure Soft wash System.</li>
      <li><svg width="18" height="18" viewBox="0 0 18 18" aria-hidden="true"><rect x="1" y="1" width="16" height="16" rx="2" fill="none" stroke="#123a5c" stroke-width="1.6"/><path d="M4.5 9.2l3 3 6-7" fill="none" stroke="#123a5c" stroke-width="2"/></svg>100% Biodegradable solutions to achieve<br>Results.</li>
      <li><svg width="18" height="18" viewBox="0 0 18 18" aria-hidden="true"><rect x="1" y="1" width="16" height="16" rx="2" fill="none" stroke="#123a5c" stroke-width="1.6"/><path d="M4.5 9.2l3 3 6-7" fill="none" stroke="#123a5c" stroke-width="2"/></svg>100% Guaranteed.</li>
    </ul>

    <p class="call">
      <svg width="22" height="22" viewBox="0 0 24 24" aria-hidden="true"><circle cx="12" cy="12" r="12" fill="#0b0b0b"/><path fill="#fff" d="M8.2 5.5l2 2.6c.3.4.3.9-.1 1.3l-1 1c.7 1.5 1.9 2.7 3.4 3.4l1-1c.4-.4.9-.4 1.3-.1l2.6 2c.4.3.5.9.1 1.3l-1.2 1.3c-.6.6-1.5.8-2.3.5-3.5-1.3-6.2-4-7.5-7.5-.3-.8-.1-1.7.5-2.3L6.9 5.4c.4-.4 1-.3 1.3.1z"/></svg>
      Call today 207-555-0148
    </p>

    <div class="service-row">
      <p class="service-mark">Roof<br>Cleaning</p>
      <span class="service-row__divider"></span>
      <p class="service-mark">House<br>Washing</p>
    </div>
  </section>

</main>
</body>
</html>
```